Marketing Brochure design required by Video Production company

We are looking for a slick, professional and eye-catching design for a marketing brochure that will showcase our company and its services.

Purpose:
The purpose of the brochure is to show our company as experienced, capable, professional and creative.

The Brochure:
The brochure will be 10 pages (including front and back cover), designed for printing in measurements of 16cm (height) x 18cm (wide).

Attached you will find:

1. Brochure Copy/Text - this is all the text to be included in the brochure. Text in red colour is not to be included in the design but is there as a guide to assist in the design

2. Design assets - our logo and hi-resolution images to be included in the design. The filenames of the images correspond with pages in the Brochure Copy/Text (as you will see)
* this does not seem to be attaching here in ArtHive. Please download this file from filetrove here: https://www.filetrove.example/s/qk4tn7wpr2xzb8h/Product_Marketing_Brochure_Assets-2016-02-07.zip?dl=0

Design:
We would like the design to be open - not cramped or squashed in. Use of space is good. We want it to look very professional, but creative. And also feel simple and easy to read.

Colours to use - blues with black & white (black & white is our brand).

Please feel free to ask any questions you might have.

Thank you.

Industry/Entity Type

It Company

Font styles to use
Sans Serif

Colors
0592cd
3176b5
3276b5
33a6d7
85cae6
cee9f5
85acd3
eaf1f7

Requirements
Must have
• As per the description.
• Download design assets from:
• https://www.filetrove.example/s/qk4tn7wpr2xzb8h/Product_Marketing_Brochure_Assets-2016-02-07.zip?dl=0

```html
<!DOCTYPE html>
<html lang="en">
<head>
<meta charset="utf-8">
<title>Lumencast – Brochure Cover</title>
<link rel="stylesheet" href="https://fonts.googleapis.com/css2?family=Jost:wght@300;400;600&display=swap">
<style>
  :root {
    --backdrop: #dcdcdc;
    --paper: #f7f7f7;
    --ink-deep: #0a0a0a;
    --ink-haze: #4a4a4a;
    --type-light: #f2f2f2;
    --type-muted: #6e6e6e;
  }
  * { margin: 0; padding: 0; box-sizing: border-box; }
  html, body {
    width: 1200px;
    height: 899px;
    overflow: hidden;
    background: var(--backdrop);
    font-family: "Jost", "Helvetica Neue", Arial, sans-serif;
  }
  .canvas {
    position: relative;
    width: 1200px;
    height: 899px;
  }
  .cover {
    position: absolute;
    left: 318px;
    top: 168px;
    width: 564px;
    height: 562px;
    background: var(--paper);
    padding: 29px 31px 29px 27px;
  }
  .cover-panel {
    position: relative;
    width: 100%;
    height: 100%;
    background:
      radial-gradient(ellipse 45% 70% at 100% 35%, rgba(110,110,110,0.55), rgba(110,110,110,0) 70%),
      linear-gradient(90deg, var(--ink-deep) 0%, var(--ink-deep) 55%, #262626 75%, var(--ink-haze) 100%);
  }
  .cover-title {
    position: absolute;
    left: 0;
    right: 0;
    top: 188px;
    text-align: center;
    color: var(--type-light);
  }
  .brand-name {
    font-weight: 600;
    font-size: 34px;
    letter-spacing: 5px;
    line-height: 1;
  }
  .title-rule {
    width: 77px;
    height: 2px;
    background: var(--type-light);
    margin: 46px auto 0;
  }
  .tagline {
    margin-top: 26px;
    font-weight: 400;
    font-size: 10px;
    letter-spacing: 2.4px;
    color: var(--type-muted);
    text-transform: uppercase;
  }
</style>
</head>
<body>
  <main class="canvas">
    <section class="cover">
      <div class="cover-panel" role="img" aria-label="Dark grainy black backdrop with soft grey light haze on the right side">
        <div class="cover-title">
          <h1 class="brand-name">LUMENCAST</h1>
          <div class="title-rule"></div>
          <p class="tagline">Creative Video Content</p>
        </div>
      </div>
    </section>
  </main>
</body>
</html>
```